Therapy Dog Organization Website

Looking for a website that is user friendly, welcoming, dog themed and has the following pages and links:
*Click here to join - links to a jot form
*Click here to donate - links to our paypal page
*Request a visit - links to a jot form
*Facebook Follow Link
*Instagram Follow Link
*Our team - images uploaded to showcase our dogs
*Donors and Referrals Page - Where I can update as donations and referrals come in.
*Online store. Currently this is in Jot Form but I would like a store front. I would not want this to be a link but rather a hidden page, something like www.hollowbirch.org/teamstore.

Please visit www.hollowbirch.org to see what we have right now designed simply in Canva. Dog photos can be provided to use in images.

Note: I have funds from a grant that I have to spend to add gratuity to the project winner.

```html
<!DOCTYPE html>
<html lang="en">
<head>
<meta charset="utf-8">
<title>Our Team – Hollow Birch Therapy Dogs</title>
<link href="https://fonts.googleapis.com/css2?family=Inter:wght@400;500;600;700&family=Playfair+Display:wght@700&display=swap" rel="stylesheet">
<style>
:root{
  --navy:#1b3a4b;
  --navy-deep:#0f2634;
  --accent:#d9875f;
  --accent-soft:#f6ece4;
  --green:#5e9680;
  --page:#f6f2ee;
  --ink:#333a40;
  --white:#ffffff;
  --footer-text:#b9c5cc;
}
*{margin:0;padding:0;box-sizing:border-box}
html,body{width:773px;height:1200px;overflow:hidden}
body{font-family:'Inter',sans-serif;background:var(--page);color:var(--ink)}
.site-header{height:53px;background:var(--white);display:flex;align-items:center;padding:0 57px;position:relative}
.brand{display:flex;align-items:center;gap:8px}
.brand-name{font-weight:700;font-size:14px;color:var(--accent);letter-spacing:-.2px}
.evaluator-badge{width:27px;height:27px;border-radius:50%;background:#3d5aa8}
.main-nav{position:absolute;left:297px;top:15px;display:flex;align-items:center;font-size:8.7px;font-weight:600;color:var(--navy)}
.main-nav a{color:inherit;text-decoration:none;padding:6px 11px;border-radius:12px}
.main-nav a.active{background:var(--navy);color:var(--white)}
.header-actions{position:absolute;right:56px;top:14px;display:flex;gap:6px}
.avatar{width:23px;height:23px;border-radius:50%;background:#8d9ba3}
.social-dot{width:23px;height:23px;border-radius:50%;background:var(--accent-soft)}
.hero{height:132px;background:linear-gradient(135deg,#1e4052,var(--navy-deep));text-align:center;color:var(--white);padding-top:33px}
.hero-title{display:flex;justify-content:center;align-items:center;gap:12px;font-family:'Playfair Display',serif;font-size:27px;line-height:1}
.hero-icon{width:29px;height:25px;border-radius:5px;background:var(--accent)}
.hero p{font-size:10.3px;line-height:17px;margin:12px auto 0;width:342px}
.team-grid{display:grid;grid-template-columns:repeat(3,208.5px);gap:17px 17px;padding:34px 57px 0}
.dog-card{background:var(--white);border-radius:12px;overflow:hidden;height:266px;position:relative}
.dog-photo{height:126px}
.status{position:absolute;top:9px;right:9px;background:var(--green);color:var(--white);font-size:7.5px;font-weight:600;padding:4px 8px;border-radius:10px}
.dog-body{padding:13px 14px 0}
.dog-name{font-family:'Playfair Display',serif;font-size:15px;color:var(--navy);line-height:18px}
.breed{font-size:8.6px;color:var(--accent);font-weight:500;margin-top:1px}
.bio{font-size:8.6px;line-height:15px;margin-top:8px;height:45px}
.tags{display:flex;gap:5px;margin-top:10px}
.tag{display:flex;align-items:center;gap:4px;background:var(--accent-soft);font-size:7.4px;font-weight:600;color:var(--navy);height:18px;padding:0 8px;border-radius:9px}
.tag svg{width:7px;height:7px;fill:var(--accent)}
.join{margin:29px 57px 0;background:var(--white);border-radius:14px;height:159px;text-align:center;padding-top:27px}
.join h2{font-family:'Playfair Display',serif;font-size:19.5px;color:var(--navy)}
.join p{font-size:9.7px;line-height:16px;width:320px;margin:6px auto 0}
.btn{display:inline-flex;align-items:center;gap:6px;margin-top:14px;background:var(--accent);color:var(--white);font-size:9.5px;font-weight:600;height:25px;padding:0 18px;border-radius:13px}
.btn svg{width:11px;height:10px;fill:var(--white)}
.site-footer{position:absolute;top:991px;left:0;width:773px;height:209px;background:var(--navy-deep);color:var(--footer-text);padding:0 57px}
.footer-brand{position:absolute;left:57px;top:38px;width:190px}
.footer-brand .brand-name{color:var(--white);font-size:14px}
.footer-brand p{font-size:9.3px;line-height:16px;margin-top:20px}
.footer-social{display:flex;gap:6px;margin-top:10px}
.footer-social span{width:24px;height:24px;border-radius:50%;background:#22404f}
.footer-col{position:absolute;top:34px}
.footer-col h3{font-size:10.3px;color:var(--white);font-weight:700;margin-bottom:9px}
.footer-col li{list-style:none;font-size:8.8px;line-height:20.5px}
.contact li{display:flex;align-items:center;gap:9px;line-height:19.5px}
.contact svg{width:8px;height:8px;fill:var(--accent)}
.footer-bottom{position:absolute;left:57px;right:57px;top:169px;border-top:1px solid #22404f;text-align:center;font-size:8.2px;color:#7f929c;padding-top:13px}
</style>
</head>
<body>
<header class="site-header">
  <div class="brand"><span class="brand-name">Hollow Birch</span><span class="evaluator-badge" role="img" aria-label="Evaluator certification badge"></span></div>
  <nav class="main-nav"><a href="#">Home</a><a class="active" href="#">Our Team</a><a href="#">Donors &amp; Referrals</a><a href="#">Store</a></nav>
  <div class="header-actions"><span class="avatar"></span><span class="social-dot" role="img" aria-label="Social media profile"></span></div>
</header>

<section class="hero">
  <h1 class="hero-title"><span class="hero-icon" role="img" aria-label="Dog icon"></span>Our Team</h1>
  <p>Meet our amazing therapy dogs and their handlers who bring comfort to our community</p>
</section>

<main class="team-grid">
  <article class="dog-card">
    <div class="dog-photo" role="img" aria-label="Photo of Sky, a white Siberian Husky in a pink bandana" style="background:linear-gradient(135deg,#8a7260,#c9c2bb 55%,#d9487f)"></div>
    <span class="status">Certified</span>
    <div class="dog-body"><h2 class="dog-name">Sky</h2><div class="breed">Siberian Husky</div>
      <p class="bio">Sky has been spreading joy for 5 years. His favorite places to visit are nursing homes where he loves to cuddle with residents.</p>
      <div class="tags"><span class="tag"><svg viewBox="0 0 10 10"><path d="M5 9L1 5A2.2 2.2 0 0 1 5 2.2 2.2 2.2 0 0 1 9 5Z"/></svg>Comfort</span><span class="tag"><svg viewBox="0 0 10 10"><path d="M5 1L1 5H2V9H8V5H9Z"/></svg>Nursing Homes</span></div></div>
  </article>
  <article class="dog-card">
    <div class="dog-photo" role="img" aria-label="Photo of Luna, a cream Siberian Husky in a pink bandana" style="background:linear-gradient(135deg,#8a7260,#d8b28c 55%,#d9487f)"></div>
    <span class="status">Certified</span>
    <div class="dog-body"><h2 class="dog-name">Luna</h2><div class="breed">Siberian Husky</div>
      <p class="bio">Luna is a gentle soul who excels at hospital visits. She has a special way of calming anxious patients.</p>
      <div class="tags"><span class="tag"><svg viewBox="0 0 10 10"><path d="M5 9L1 5A2.2 2.2 0 0 1 5 2.2 2.2 2.2 0 0 1 9 5Z"/></svg>Comfort</span><span class="tag"><svg viewBox="0 0 10 10"><path d="M1 9V3H4V1H6V3H9V9Z"/></svg>Hospitals</span></div></div>
  </article>
  <article class="dog-card">
    <div class="dog-photo" role="img" aria-label="Photo of Nova, a merle Pomsky in a pink bandana" style="background:linear-gradient(135deg,#7a6555,#9aa0a6 55%,#d9487f)"></div>
    <span class="status">Certified</span>
    <div class="dog-body"><h2 class="dog-name">Nova</h2><div class="breed">Pomsky</div>
      <p class="bio">Nova is our star school visitor. Children love his playful personality and he's great at helping kids read aloud.</p>
      <div class="tags"><span class="tag"><svg viewBox="0 0 10 10"><path d="M5 2L0 4.5 5 7 10 4.5ZM2.5 6V8H7.5V6L5 7.3Z"/></svg>Schools</span><span class="tag"><svg viewBox="0 0 10 10"><path d="M2 1H8V9H2Z"/></svg>Reading</span></div></div>
  </article>
  <article class="dog-card">
    <div class="dog-photo" role="img" aria-label="Photo of Elliott, a Doberman Pinscher in a blue bandana under a blue sky" style="background:linear-gradient(135deg,#3f8fd6,#8a5a40 55%,#2d4c8a)"></div>
    <span class="status">In Training</span>
    <div class="dog-body"><h2 class="dog-name">Elliott</h2><div class="breed">Doberman Pinscher</div>
      <p class="bio">Elliott is currently completing his therapy dog certification. He's showing great promise in disaster response work.</p>
      <div class="tags"><span class="tag"><svg viewBox="0 0 10 10"><path d="M5 1C7 3 8 5 8 6.5A3 3 0 0 1 2 6.5C2 5 3 4 4 3 4 4 5 4.5 5 1Z"/></svg>Disaster Response</span></div></div>
  </article>
  <article class="dog-card">
    <div class="dog-photo" role="img" aria-label="Photo of Lupo, a black German Shepherd" style="background:linear-gradient(135deg,#6b4a35,#2a2420 55%,#4a3528)"></div>
    <span class="status">Certified</span>
    <div class="dog-body"><h2 class="dog-name">Lupo</h2><div class="breed">German Shepherd</div>
      <p class="bio">Lupo brings smiles wherever she goes. Her upbeat energy makes her perfect for children's hospital visits.</p>
      <div class="tags"><span class="tag"><svg viewBox="0 0 10 10"><path d="M5 9L1 5A2.2 2.2 0 0 1 5 2.2 2.2 2.2 0 0 1 9 5Z"/></svg>Comfort</span><span class="tag"><svg viewBox="0 0 10 10"><path d="M1 9V3H4V1H6V3H9V9Z"/></svg>Children's Hospital</span></div></div>
  </article>
  <article class="dog-card">
    <div class="dog-photo" role="img" aria-label="Photo of Koa, a brindle Dutch Shepherd against a cloudy blue sky" style="background:linear-gradient(135deg,#3d8fc9,#4a3a30 55%,#8fbfe0)"></div>
    <span class="status">Certified</span>
    <div class="dog-body"><h2 class="dog-name">Koa</h2><div class="breed">Dutch Shepherd</div>
      <p class="bio">Koa is hypoallergenic and perfect for visits where allergies are a concern. He's calm and dignified.</p>
      <div class="tags"><span class="tag"><svg viewBox="0 0 10 10"><path d="M3 9V4H7V9ZM3 4V1H4V4ZM4.5 4V1H5.5V4ZM6 4V1.5H7V4Z"/></svg>Hypoallergenic</span><span class="tag"><svg viewBox="0 0 10 10"><path d="M2 1H8V9H2Z"/></svg>Offices</span></div></div>
  </article>
</main>

<section class="join">
  <h2>Want to Join Our Pack?</h2>
  <p>We're always looking for new therapy dog teams. If you and your dog have what it takes, we'd love to hear from you!</p>
  <a class="btn"><svg viewBox="0 0 12 10"><circle cx="4" cy="3" r="2.3"/><path d="M0 10C0 7 2 6 4 6S8 7 8 10Z M9 2H10V3.5H11.5V4.5H10V6H9V4.5H7.5V3.5H9Z"/></svg>Apply to Join</a>
</section>

<footer class="site-footer">
  <div class="footer-brand"><span class="brand-name">Hollow Birch</span>
    <p>Bringing comfort, joy and unconditional love — One Paw at a time.</p>
    <div class="footer-social"><span role="img" aria-label="Social media profile"></span><span role="img" aria-label="Social media profile"></span></div></div>
  <div class="footer-col" style="left:295px"><h3>Quick Links</h3><ul><li>Home</li><li>Our Team</li><li>Donors &amp; Referrals</li><li>Team Store</li></ul></div>
  <div class="footer-col" style="left:425px"><h3>Get Involved</h3><ul><li>Join Our Pack</li><li>Request a Visit</li><li>Donate</li></ul></div>
  <div class="footer-col contact" style="left:555px"><h3>Contact Us</h3><ul>
    <li><svg viewBox="0 0 10 10"><path d="M0 2H10V8H0ZM0 2L5 5.5 10 2V3L5 6.5 0 3Z"/></svg>info@hollowbirch.org</li>
    <li><svg viewBox="0 0 10 10"><path d="M2 0.5L4 2.5 3 4C4 6 5 7 6.5 7.5L8 6.5 9.8 8.3 8.5 9.8C4 9.5 0.5 6 0.3 1.5Z"/></svg>(555) 010-4821</li></ul></div>
  <div class="footer-bottom">© 2026 Hollow Birch Therapy Dogs. All rights reserved.</div>
</footer>
</body>
</html>
```